Eye catching business card

2 sided
Black background with logo in color on one side along with the words "Proudly serving the commercial and defense industries since 1975"
2nd side to contain contact information (see attached current business card) and "Waterjet, Composite, Precision Machining and Clean Room Manufacturing" with a very faint watermark of a waving USA Flag in the back ground.
Remove the "est. 195" from the current logo design

```html
<!DOCTYPE html>
<html lang="en">
<head>
<meta charset="utf-8">
<title>Ridgeline Machine Works – Business Card</title>
<link href="https://fonts.googleapis.com/css2?family=Arimo:wght@400;700&display=swap" rel="stylesheet">
<style>
  :root {
    --bg: #7a7a7a;
    --card-black: #000000;
    --card-white: #ffffff;
    --brand-blue: #1f63c9;
    --bar-blue-edge: #2a72d2;
    --bar-blue-mid: #2aaee3;
    --steel: #9a9a9a;
    --text-grey: #7d7d7d;
  }
  * { box-sizing: border-box; margin: 0; padding: 0; }
  html, body { width: 1200px; height: 1200px; overflow: hidden; }
  body {
    background: var(--bg);
    font-family: "Arimo", Arial, sans-serif;
    position: relative;
  }
  .card {
    position: absolute;
    left: 242px;
    width: 716px;
    height: 410px;
    overflow: hidden;
  }
  /* Front side */
  .card--front { top: 170px; background: var(--card-black); }
  .brand-front {
    position: absolute;
    left: 0; right: 0; top: 150px;
    display: flex; align-items: center; justify-content: center; gap: 14px;
  }
  .brand-square { width: 30px; height: 30px; background: var(--brand-blue); }
  .brand-name {
    color: var(--steel);
    font-weight: 700;
    font-size: 38px;
    letter-spacing: 1px;
    text-transform: uppercase;
  }
  .tagline-band {
    position: absolute;
    left: 0; right: 0; top: 331px; height: 35px;
    background: var(--card-white);
    display: flex; align-items: center; justify-content: center;
    color: var(--brand-blue);
    font-weight: 700;
    font-size: 16.5px;
  }
  /* Back side */
  .card--back { top: 620px; background: var(--card-white); }
  .edge-bar {
    position: absolute; left: 0; right: 0; height: 37px;
    background: linear-gradient(90deg, var(--bar-blue-edge), var(--bar-blue-mid) 50%, var(--bar-blue-edge));
  }
  .edge-bar--top { top: 0; }
  .edge-bar--bottom { bottom: 0; }
  .brand-back {
    position: absolute; left: 38px; width: 284px; top: 120px;
    display: flex; flex-direction: column; align-items: center; gap: 14px;
  }
  .brand-back .brand-square { width: 42px; height: 42px; }
  .brand-back .brand-name { font-size: 25px; letter-spacing: 0; text-align: center; line-height: 1.15; }
  .divider {
    position: absolute; left: 357px; top: 67px; width: 3px; height: 179px;
    background: var(--brand-blue);
  }
  .contact { position: absolute; left: 386px; top: 68px; }
  .contact-name { color: var(--brand-blue); font-weight: 700; font-size: 29px; line-height: 1; }
  .contact-title { color: var(--text-grey); font-weight: 700; font-size: 21px; margin-top: 8px; }
  .contact-line { color: var(--brand-blue); font-size: 22px; font-weight: 700; }
  .contact-line--office { margin-top: 38px; }
  .contact-line--email { margin-top: 10px; }
  .contact-label { font-weight: 400; }
  .services {
    position: absolute; left: 0; right: 0; top: 266px;
    text-align: center; color: var(--brand-blue);
    font-weight: 700; font-size: 23px; line-height: 28px;
  }
  .address {
    position: absolute; left: 0; right: 0; top: 327px;
    text-align: center; color: var(--text-grey);
    font-weight: 700; font-size: 13.5px; line-height: 17px;
  }
</style>
</head>
<body>
  <section class="card card--front" aria-label="Business card front">
    <div class="brand-front">
      <span class="brand-square"></span>
      <span class="brand-name">Ridgeline Machine Works</span>
    </div>
    <div class="tagline-band">Proudly serving the commercial and defense industries since 1975.</div>
  </section>

  <section class="card card--back" aria-label="Business card back">
    <div class="edge-bar edge-bar--top"></div>
    <div class="brand-back">
      <span class="brand-square"></span>
      <span class="brand-name">Ridgeline Machine Works</span>
    </div>
    <div class="divider"></div>
    <div class="contact">
      <p class="contact-name">DALE MERCER</p>
      <p class="contact-title">President</p>
      <p class="contact-line contact-line--office"><span class="contact-label">Office:</span> 555-204-3100</p>
      <p class="contact-line contact-line--email">dale@ridgelinemw.com</p>
    </div>
    <p class="services">Waterjet, Composite, Precision Machining<br>and Clean Room Manufacturing</p>
    <p class="address">214 Orchard Mill Rd. Glen Hollow, PA 17020 • Phone: 555-204-3100 • Fax: 555-204-3140<br>info@ridgelinemw.com • www.ridgelinemw.com</p>
    <div class="edge-bar edge-bar--bottom"></div>
  </section>
</body>
</html>
```